TalkBridge - Language Coaching Services

Sleek, innovative, trendy design for Language Coaching business.

TalkBridge is a new UK based company that provides Language Coaching services. We offer highly personalized on-line and face to face language courses. We also impart learning techniques workshops based on the latest neuroscience research for second-language acquisition.

Target Market(s)

Industry/Entity Type

Consulting

Contact Information for Business Card

TalkBridge
ElenaVT@talkbridge-demo.co.uk
TalkBridge-demo.co.uk
London, UK

Font styles to use
Sans Serif

```html
<!DOCTYPE html>
<html lang="en">
<head>
<meta charset="utf-8">
<title>TalkBridge – Business Card</title>
<link href="https://fonts.googleapis.com/css2?family=Questrial&family=Arimo:wght@400;700&display=swap" rel="stylesheet">
<style>
  :root {
    --page-bg: #2b2b2b;
    --brand-blue: #1a5f86;
    --brand-blue-deep: #0f4566;
    --brand-blue-light: #2a7aa6;
    --card-white: #f7f7f7;
    --text-light: #dce9f1;
    --divider: #6d95ad;
  }
  * { margin: 0; padding: 0; box-sizing: border-box; }
  html, body { width: 1200px; height: 997px; overflow: hidden; }
  body { background: var(--page-bg); position: relative; font-family: "Arimo", Arial, sans-serif; }

  .card {
    position: absolute;
    width: 560px;
    height: 320px;
    overflow: hidden;
    box-shadow: 0 12px 30px rgba(0,0,0,0.45);
  }

  /* Back of card */
  .card-back {
    left: 110px;
    top: 110px;
    background: linear-gradient(135deg, var(--brand-blue-light), var(--brand-blue) 55%, var(--brand-blue-deep));
    display: flex;
    flex-direction: column;
    align-items: center;
    justify-content: center;
    gap: 18px;
  }
  .card-back .brand-dot {
    width: 110px; height: 110px;
    border: 10px solid #ffffff;
    border-radius: 50%;
  }
  .card-back .brand-name {
    font-family: "Questrial", Arial, sans-serif;
    font-size: 40px;
    letter-spacing: 3px;
    color: #ffffff;
    text-transform: uppercase;
  }

  /* Front of card */
  .card-front {
    left: 530px;
    top: 520px;
    background: linear-gradient(160deg, #ffffff, var(--card-white) 60%, #e9e9e9);
  }
  .card-front .wave { position: absolute; inset: 0; }
  .card-front .brand {
    position: absolute;
    left: 0; right: 0; top: 22px;
    display: flex;
    flex-direction: column;
    align-items: center;
    gap: 10px;
  }
  .card-front .brand-dot {
    width: 62px; height: 62px;
    border: 6px solid var(--brand-blue);
    border-radius: 50%;
  }
  .card-front .brand-name {
    font-family: "Questrial", Arial, sans-serif;
    font-size: 44px;
    letter-spacing: 3px;
    color: var(--brand-blue);
    text-transform: uppercase;
    line-height: 1;
  }

  .contact-block {
    position: absolute;
    left: 220px;
    top: 225px;
    display: flex;
    align-items: center;
    gap: 16px;
    color: var(--text-light);
  }
  .person { text-align: right; }
  .person-name { font-weight: 700; font-size: 15px; letter-spacing: 0.5px; }
  .person-role { font-size: 14px; }
  .divider { width: 1px; height: 44px; background: var(--divider); }
  .contact-list { list-style: none; display: flex; flex-direction: column; gap: 8px; font-size: 13px; }
  .contact-list li { display: flex; align-items: center; gap: 8px; }
  .contact-icon { width: 14px; height: 14px; flex: none; }
</style>
</head>
<body>

  <section class="card card-back" aria-label="Business card, back">
    <span class="brand-dot" aria-hidden="true"></span>
    <span class="brand-name">TalkBridge</span>
  </section>

  <section class="card card-front" aria-label="Business card, front">
    <svg class="wave" viewBox="0 0 560 320" preserveAspectRatio="none" aria-hidden="true">
      <path d="M0,320 L0,265 Q230,175 560,172 L560,320 Z" fill="var(--brand-blue)"/>
      <path d="M0,320 L0,290 Q240,205 560,195 L560,320 Z" fill="var(--brand-blue-deep)" opacity="0.45"/>
      <path d="M40,238 Q260,150 540,150" fill="none" stroke="var(--brand-blue)" stroke-width="3" stroke-linecap="round"/>
    </svg>

    <div class="brand">
      <span class="brand-dot" aria-hidden="true"></span>
      <span class="brand-name">TalkBridge</span>
    </div>

    <div class="contact-block">
      <div class="person">
        <p class="person-name">MARCUS HALE</p>
        <p class="person-role">Director</p>
      </div>
      <span class="divider" aria-hidden="true"></span>
      <ul class="contact-list">
        <li>
          <svg class="contact-icon" viewBox="0 0 14 14" aria-hidden="true">
            <circle cx="7" cy="7" r="7" fill="var(--text-light)"/>
            <path d="M4 5 Q7 3 10 5 L9.5 6.5 L8.5 6 L8.5 5.3 Q7 4.9 5.5 5.3 L5.5 6 L4.5 6.5 Z M4.5 8 H9.5 V10 H4.5 Z" fill="var(--brand-blue)"/>
          </svg>
          <span>0491 570 156</span>
        </li>
        <li>
          <svg class="contact-icon" viewBox="0 0 14 14" aria-hidden="true">
            <circle cx="7" cy="7" r="7" fill="var(--text-light)"/>
            <rect x="3.5" y="4.5" width="7" height="5" fill="var(--brand-blue)"/>
            <path d="M3.5 4.5 L7 7.5 L10.5 4.5" fill="none" stroke="var(--text-light)" stroke-width="0.8"/>
          </svg>
          <span>marcus@northbay-demo.com.au</span>
        </li>
      </ul>
    </div>
  </section>

</body>
</html>
```